Web Site Design for a Finance (lending) Company

We are opening a new subsidiary that focuses on lending money in the real estate industry. We need a web site designed to represent the business.

The business is lending money to real estate investors. A typical client/borrower will be looking to borrow money to buy a house, renovate it and then sell it at a profit, all within 12 months or less.

Company name is Brevand Finance. Our logo is attached.

Attached is a general outline for the web site. We're working on writing more text for each page but this should give you enough to get started with some ideas.

Competitor web site that I like a lot (as an example): https://quorvelfunding.com/. Many of the general items on this site match what we will need (description of loan programs, FAQ)

Target Market(s)

Real estate investors (generally individuals or small companies with just a few people) who are buying homes, renovating them and then selling them at a profit.

Industry/Entity Type

Finance

Coding

Coded - Design and coding required

Number of Pages Required

5+ page

Colors

Designer to choose colors to be used in the design.

Requirements
Must have
• Minimalist design. Clean lines without too much clutter. Some stock photography is ok but the photos should not be distracting. They should almost fade in to the background so that user can focus on the key information about what our company does instead. We are a finance company, not a design company, so the information about our products will be more interesting to site visitors than the art.
• Some minimalist examples from Snapboard:
• https://www.snapboard-example.com/explore/minimalist-web-design/
Nice to have
• If you search in seekly for "hard money lenders" you will find many examples of web sites from our competition. I have provided a link above to competitor web site that I like a lot.
• I have attached our logo in EPS format. Logo is green. Web site doesn't have to be green but it should be of a color that will work well with the logo.

```html
<!DOCTYPE html>
<html lang="en">
<head>
<meta charset="utf-8">
<title>Brevand Finance</title>
<link href="https://fonts.googleapis.com/css2?family=Poppins:wght@300;400;500;600&display=swap" rel="stylesheet">
<style>
:root{
  --navy:#24344a;
  --navy-line:#3a4a60;
  --green:#6c9a3b;
  --sky:#00acee;
  --pale:#edf5fc;
  --ink:#2b2f36;
  --muted:#6d7580;
  --white:#ffffff;
}
*{margin:0;padding:0;box-sizing:border-box}
html,body{width:1200px;height:3495px;overflow:hidden}
body{position:relative;font-family:'Poppins',sans-serif;color:var(--ink);background:var(--white)}
.abs{position:absolute}
a{color:inherit;text-decoration:none}

/* header */
.site-header{left:0;top:0;width:1200px;height:82px;background:var(--navy)}
.brand{left:158px;top:18px;display:flex;align-items:center;gap:10px;color:var(--white);font-size:18px;font-weight:500;line-height:1.05}
.brand-mark{width:14px;height:14px;background:var(--green)}
.main-nav{left:403px;top:30px;display:flex;gap:38px;font-size:13px;color:#dfe6ee}
.main-nav .active{color:var(--green)}
.apply-btn{left:932px;top:28px;width:112px;height:32px;border-radius:16px;background:var(--green);color:var(--white);font-size:12px;font-weight:500;display:flex;align-items:center;justify-content:center}

/* hero */
.hero-photo{left:0;top:82px;width:1200px;height:436px;background:linear-gradient(90deg,#eef1f3 0%,#e7ecef 40%,#cfd9df 62%,#9fb6c6 78%,#c9d3d9 100%)}
.hero-title{left:156px;top:192px;font-size:32px;font-weight:500;color:var(--ink)}
.hero-sub{left:156px;top:236px;font-size:23px;line-height:1.3;color:var(--ink)}
.hero-sub strong{font-weight:600}
.pill{border-radius:16px;background:var(--green);color:var(--white);font-size:11px;font-weight:500;display:flex;align-items:center;justify-content:center}
.discover-btn{left:158px;top:322px;width:127px;height:32px}

/* intro */
.pale-band{left:0;top:518px;width:1200px;height:710px;background:var(--pale)}
.features{left:156px;top:473px;width:888px;height:207px;background:var(--sky);display:flex}
.feature{flex:1;padding:36px 30px 0;color:var(--white);border-right:1px solid rgba(255,255,255,.3)}
.feature:last-child{border-right:0}
.feature h3{font-size:14px;font-weight:400;margin:22px 0 6px}
.feature p{font-size:11px;line-height:1.5;font-weight:300;width:230px}
.feature-dot{left:190px;top:665px;width:30px;height:30px;border-radius:50%;background:var(--white);border:1px solid #cfd8e0}
.intro-text{left:280px;top:735px;width:640px;text-align:center;font-size:16px;line-height:1.7;color:#444}
.about-btn{left:508px;top:860px;width:184px;height:32px}

.section-title{left:0;width:1200px;display:flex;justify-content:center;align-items:center;gap:22px;font-size:24px;font-weight:400;color:var(--ink)}
.section-title::before,.section-title::after{content:"";width:62px;height:1px;background:#9aa3ad}
.loans-title{top:946px}

.loan-card{top:1007px;width:357px;height:398px;background:var(--pale)}
.loan-photo{height:221px}
.loan-body{padding:22px 24px 0}
.loan-body h3{font-size:15px;font-weight:500;margin-bottom:10px}
.loan-body p{font-size:12px;line-height:1.55;color:var(--muted);width:300px}
.loan-link{display:inline-block;margin-top:24px;font-size:11px;padding-bottom:3px;border-bottom:1px solid var(--ink)}
.loan-link.live{color:var(--green);border-color:var(--green)}

/* work gallery */
.work-title{top:1458px}
.tile{position:absolute}
.tile-overlay{left:424px;top:1522px;width:352px;height:186px;background:rgba(36,52,74,.62);display:flex;flex-direction:column;align-items:center;justify-content:center;color:var(--white);font-size:14px;gap:10px}
.ghost-btn{border:2px solid #c9dbb5;border-radius:18px;font-size:11px;color:var(--ink);display:flex;align-items:center;justify-content:center;background:var(--white)}
.work-btn{left:534px;top:1946px;width:130px;height:34px}

/* testimonial */
.quote-band{left:0;top:2044px;width:1200px;height:389px;background:linear-gradient(180deg,#4a5a6b,#3a4858)}
.quote-text{left:300px;top:2180px;width:600px;text-align:center;color:var(--white);font-size:16px;line-height:1.75;font-weight:300}
.quote-name{left:0;top:2318px;width:1200px;display:flex;justify-content:center;align-items:center;gap:10px;color:var(--white);font-size:13px}
.quote-name::before,.quote-name::after{content:"";width:40px;height:1px;background:rgba(255,255,255,.6)}
.quote-dots{left:570px;top:2370px;display:flex;gap:8px}
.quote-dots span{width:10px;height:10px;transform:rotate(45deg);border:1px solid rgba(255,255,255,.8)}
.quote-dots .on{background:var(--white)}

/* blog */
.blog-title{left:154px;top:2494px;display:flex;align-items:center;gap:18px;font-size:22px}
.blog-title::after{content:"";width:62px;height:1px;background:#9aa3ad}
.round-btn{width:24px;height:24px;border-radius:50%;display:flex;align-items:center;justify-content:center}
.round-btn.plain{border:1px solid #aab2bb;background:var(--white)}
.round-btn.solid{background:var(--green)}
.post{top:2550px;width:282px}
.post-photo{height:174px}
.post-date{font-size:11px;color:var(--muted);margin:18px 0 8px}
.post-date.live{color:var(--green)}
.post p{font-size:14px;line-height:1.6;color:#444}
.post p.live u{text-decoration:none;border-bottom:1px solid #444}
.blog-btn{left:534px;top:2855px;width:114px;height:34px}

/* trusted */
.trust-title{top:2944px}
.partner{top:3001px;height:79px;background:#f1f3f5;display:flex;align-items:center;justify-content:center;gap:8px;font-size:20px;font-weight:500;color:#2a4a8a}
.partner .sq{width:14px;height:14px;background:#2a4a8a}

/* footer */
.site-footer{left:0;top:3146px;width:1200px;height:349px;background:var(--navy);color:#cfd7e0}
.foot-brand{left:156px;top:3206px;font-size:22px;color:var(--green);font-weight:500}
.foot-call{left:156px;top:3248px;font-size:18px;color:#aeb8c3;font-weight:300}
.foot-mail{left:156px;top:3276px;font-size:12px;color:#aeb8c3}
.social{left:156px;top:3318px;display:flex;gap:8px}
.social span{width:20px;height:20px;border-radius:50%;background:#dfe6ee}
.foot-rule{left:156px;top:3384px;width:329px;height:1px;background:var(--navy-line)}
.foot-split{left:485px;top:3146px;width:1px;height:300px;background:var(--navy-line)}
.copyright{left:156px;top:3410px;font-size:10px;color:#9aa6b3}
.form-title{left:536px;top:3206px;font-size:14px;color:var(--white);font-weight:500}
.field{left:536px;width:380px;border-bottom:1px solid var(--navy-line);font-size:11px;color:#b8c2cd;padding-bottom:8px}
.send-btn{left:536px;top:3398px;width:93px;height:30px;gap:6px}
.chat{left:985px;top:3214px;width:80px;text-align:center;font-size:11px;color:#cfd7e0}
.to-top{left:996px;top:3396px}
.dot-blue{left:480px;top:3448px;width:10px;height:10px;border-radius:50%;background:var(--sky)}
</style>
</head>
<body>

<header class="abs site-header">
  <div class="abs brand"><span class="brand-mark"></span><span>Brevand<br>Finance</span></div>
  <nav class="abs main-nav">
    <a class="active" href="#">Home</a><a href="#">About Us ▾</a><a href="#">Loans</a><a href="#">Resources ▾</a><a href="#">Contact Us</a><a href="#">Login</a>
  </nav>
  <a class="abs apply-btn" href="#">Apply Now!</a>
</header>

<div class="abs hero-photo" role="img" aria-label="Photo of two smiling investors reviewing plans at a laptop in a bright office"></div>
<h1 class="abs hero-title">Brevand Finance</h1>
<p class="abs hero-sub">The Nation's Premier Lender for<br><strong>Real Estate Investors</strong></p>
<a class="abs pill discover-btn" href="#">Discover More</a>

<div class="abs pale-band"></div>
<section class="abs features">
  <div class="feature">
    <svg width="52" height="52" viewBox="0 0 52 52" fill="none" stroke="#fff" stroke-width="2"><rect x="24" y="6" width="22" height="16" rx="2"/><circle cx="16" cy="26" r="7"/><path d="M4 46c0-8 5-12 12-12s12 4 12 12"/></svg>
    <h3>Experts</h3><p>There are many variations of passages of Lorem Ipsum available...</p>
  </div>
  <div class="feature">
    <svg width="52" height="52" viewBox="0 0 52 52" fill="none" stroke="#fff" stroke-width="2"><circle cx="24" cy="26" r="19"/><path d="M14 26l8 8 22-22"/></svg>
    <h3>Fast Approval</h3><p>There are many variations of passages of Lorem Ipsum available...</p>
  </div>
  <div class="feature">
    <svg width="52" height="52" viewBox="0 0 52 52" fill="none" stroke="#fff" stroke-width="2"><path d="M44 20A19 19 0 1 0 44 32"/><path d="M44 12v8h-8"/><text x="19" y="32" fill="#fff" stroke="none" font-size="16" font-family="Poppins,sans-serif">$</text></svg>
    <h3>Competitive Rates &amp; Fees</h3><p>There are many variations of passages of Lorem Ipsum available...</p>
  </div>
</section>
<div class="abs feature-dot"></div>

<p class="abs intro-text">Contrary to popular belief, Lorem Ipsum is not simply random text. It has roots in a piece of classical Latin literature from 45 BC, making it over 2000 years old. Rowan Kessler, a Latin professor at Ashford Hill College in...</p>
<a class="abs pill about-btn" href="#">Explore More About Us</a>

<h2 class="abs section-title loans-title">Loans Offered</h2>
<article class="abs loan-card" style="left:231px">
  <div class="loan-photo" role="img" aria-label="Photo of a small model house on a desk beside paperwork" style="background:linear-gradient(135deg,#c9d4de,#e6ecf1 55%,#b7a58e)"></div>
  <div class="loan-body"><h3>Fix and Flip Loans</h3><p>Contrary to popular belief, Lorem Ipsum is not simply random text. It has roots in a piece of classical Latin literature from...</p><a class="loan-link" href="#">Explore More</a></div>
</article>
<article class="abs loan-card" style="left:610px">
  <div class="loan-photo" role="img" aria-label="Photo of a modern glass commercial building against the sky" style="background:linear-gradient(135deg,#d9e2ea,#9fb1c1 50%,#e9eef2)"></div>
  <div class="loan-body"><h3>Commercial Hard Money Loans</h3><p>Contrary to popular belief, Lorem Ipsum is not simply random text. It has roots in a piece of classical Latin literature from...</p><a class="loan-link live" href="#">Explore More</a></div>
</article>

<h2 class="abs section-title work-title">See How It's Worked For Others</h2>
<div class="tile" role="img" aria-label="Photo of a two-storey family house with lit windows at dusk" style="left:49px;top:1522px;width:349px;height:398px;background:linear-gradient(180deg,#9aa7c8,#c9b7c6 40%,#5e6c82 75%,#7a8a6a)"></div>
<div class="tile" role="img" aria-label="Photo looking up at tall office towers" style="left:424px;top:1522px;width:352px;height:186px;background:linear-gradient(180deg,#8e9aa6,#55626f)"></div>
<div class="abs tile-overlay">
  <svg width="36" height="36" viewBox="0 0 36 36" fill="none" stroke="#fff" stroke-width="1.5"><circle cx="18" cy="18" r="16"/><path d="M18 10v16M10 18h16"/></svg>
  <span>Linden Heights, OH</span>
</div>
<div class="tile" role="img" aria-label="Photo of a white house with a green lawn under a blue sky" style="left:424px;top:1734px;width:352px;height:186px;background:linear-gradient(180deg,#8fb6db,#dfe7ea 45%,#6f9a4a 75%,#4f7a35)"></div>
<div class="tile" role="img" aria-label="Photo of a white cottage with a steep roof and blue door" style="left:799px;top:1522px;width:352px;height:398px;background:linear-gradient(180deg,#6fa9dc,#dde8ee 35%,#f3f3f0 60%,#b9ab96)"></div>
<a class="abs ghost-btn work-btn" href="#">View All Work</a>

<section class="abs quote-band" role="img" aria-label="Dimmed photo of a living room with plants and bookshelves"></section>
<svg class="abs" style="left:572px;top:2098px" width="56" height="50" viewBox="0 0 56 50" fill="none" stroke="#fff" stroke-width="2.5"><path d="M6 6h34a4 4 0 0 1 4 4v20a4 4 0 0 1-4 4H22l-10 9v-9H6a4 4 0 0 1-4-4V10a4 4 0 0 1 4-4z"/><text x="15" y="29" fill="#fff" stroke="none" font-size="20" font-family="Poppins,sans-serif">“”</text></svg>
<p class="abs quote-text">Sed ut perspiciatis unde omnis iste natus sit voluptatem set accusantium doloremque laudantium, totam rem aperiam such a great theme, and Nemo enim ipsam There are many passages All the Lorem Ipsum generators...</p>
<p class="abs quote-name">Delia Marsh</p>
<div class="abs quote-dots"><span></span><span class="on"></span><span></span></div>

<h2 class="abs blog-title">Latest Blog</h2>
<div class="abs round-btn plain" style="left:992px;top:2500px"><svg width="8" height="10" viewBox="0 0 8 10"><path d="M6 1L2 5l4 4" stroke="#555" stroke-width="1.6" fill="none"/></svg></div>
<div class="abs round-btn solid" style="left:1020px;top:2500px"><svg width="8" height="10" viewBox="0 0 8 10"><path d="M2 1l4 4-4 4" stroke="#fff" stroke-width="1.6" fill="none"/></svg></div>
<article class="abs post" style="left:154px"><div class="post-photo" role="img" aria-label="Photo of a laptop showing charts on a desk" style="background:linear-gradient(135deg,#e8ecef,#b9c2ca 60%,#7b858f)"></div><p class="post-date">May 22, 2017</p><p>Contrary to popular belief,<br>Lorem Ipsum is...</p></article>
<article class="abs post" style="left:459px"><div class="post-photo" role="img" aria-label="Top-down photo of a team meeting around a table" style="background:linear-gradient(135deg,#5b6168,#c9c3b8 50%,#3e444a)"></div><p class="post-date">Jun 10, 2017</p><p>Contrary to popular belief,<br>Lorem Ipsum is...</p></article>
<article class="abs post" style="left:764px"><div class="post-photo" role="img" aria-label="Photo of a businessman gesturing at a desk" style="background:linear-gradient(135deg,#2f3f63,#8ea0bd 55%,#dfe5ec)"></div><p class="post-date live">Sept 15, 2017</p><p class="live"><u>Contrary to popular belief,</u><br><u>Lorem Ipsum is...</u></p></article>
<a class="abs ghost-btn blog-btn" href="#">View All</a>

<h2 class="abs section-title trust-title">We are Trusted by Many</h2>
<div class="abs round-btn plain" style="left:107px;top:3029px"><svg width="8" height="10" viewBox="0 0 8 10"><path d="M6 1L2 5l4 4" stroke="#555" stroke-width="1.6" fill="none"/></svg></div>
<div class="abs partner" style="left:154px;width:207px"><span class="sq"></span>Norvik</div>
<div class="abs partner" style="left:398px;width:180px">Datawise</div>
<div class="abs partner" style="left:613px;width:203px">Kelvora</div>
<div class="abs partner" style="left:839px;width:205px"><span class="sq"></span>Halden</div>
<div class="abs round-btn solid" style="left:1068px;top:3029px"><svg width="8" height="10" viewBox="0 0 8 10"><path d="M2 1l4 4-4 4" stroke="#fff" stroke-width="1.6" fill="none"/></svg></div>

<footer class="abs site-footer"></footer>
<div class="abs foot-brand">Brevand Finance</div>
<div class="abs foot-call">Call Us: 555-018-2046</div>
<div class="abs foot-mail">hello@brevandfinance.com</div>
<div class="abs social"><span></span><span></span><span></span><span></span></div>
<div class="abs foot-rule"></div>
<div class="abs foot-split"></div>
<p class="abs copyright">© 2017 - Brevand Finance. All Rights Reserved</p>
<p class="abs form-title">Get in touch with us</p>
<div class="abs field" style="top:3250px">Name</div>
<div class="abs field" style="top:3297px">Email</div>
<div class="abs field" style="top:3348px">Message</div>
<a class="abs pill send-btn" href="#"><svg width="12" height="10" viewBox="0 0 12 10"><path d="M0 0l12 5-12 5 2-5z" fill="#fff"/></svg>Send</a>
<div class="abs chat">
  <svg width="30" height="30" viewBox="0 0 30 30" fill="none" stroke="#6c9a3b" stroke-width="2"><circle cx="15" cy="14" r="11"/><path d="M8 24l-3 4 7-2"/><circle cx="11" cy="14" r="1" fill="#6c9a3b"/><circle cx="15" cy="14" r="1" fill="#6c9a3b"/><circle cx="19" cy="14" r="1" fill="#6c9a3b"/></svg>
  <div>Live Chat</div>
</div>
<svg class="abs to-top" width="32" height="34" viewBox="0 0 32 34" fill="none" stroke="#7fb3e0" stroke-width="2"><path d="M16 28V6M7 15l9-9 9 9M4 32h24"/></svg>
<div class="abs dot-blue"></div>

</body>
</html>
```